Women's Health Company needs business card

We need a business card for a USA based women's health care company. We use digital technology to enhance therapy prescribed by clinicians for their patients

```html
<!DOCTYPE html>
<html lang="en">
<head>
<meta charset="utf-8">
<title>Veyla Health – Business Card</title>
<link href="https://fonts.googleapis.com/css2?family=Josefin+Sans:wght@400&family=Great+Vibes&display=swap" rel="stylesheet">
<style>
  :root {
    --backdrop: #b5b5b5;
    --card-white: #ffffff;
    --violet-front: #9f4db3;
    --violet-back: #85479a;
    --teal: #6cc5c0;
    --ink-light: #ffffff;
  }
  * { margin: 0; padding: 0; box-sizing: border-box; }
  html, body {
    width: 1200px;
    height: 900px;
    overflow: hidden;
    background: var(--backdrop);
    font-family: "Josefin Sans", sans-serif;
  }
  .canvas {
    position: relative;
    width: 1200px;
    height: 900px;
  }
  .card {
    position: absolute;
    left: 290px;
    width: 620px;
    height: 354px;
    overflow: hidden;
    box-shadow: 0 8px 24px rgba(0,0,0,0.18);
  }
  .card--front { top: 60px; background: var(--card-white); }
  .card--back { top: 486px; background: var(--violet-back); }
  .card__waves {
    position: absolute;
    inset: 0;
    width: 100%;
    height: 100%;
  }
  .brand {
    position: absolute;
    display: flex;
    align-items: center;
    gap: 8px;
    color: var(--teal);
    font-weight: 400;
    white-space: nowrap;
  }
  .brand__dot {
    width: 10px;
    height: 10px;
    border-radius: 50%;
    background: var(--violet-front);
  }
  .card--front .brand {
    right: 48px;
    top: 70px;
    font-size: 46px;
  }
  .card--back .brand {
    left: 46px;
    bottom: 46px;
    font-size: 26px;
  }
  .card--back .brand__dot { width: 7px; height: 7px; }
  .person {
    position: absolute;
    left: 44px;
    top: 138px;
    color: var(--ink-light);
  }
  .person__name {
    font-family: "Great Vibes", cursive;
    font-size: 44px;
    line-height: 1;
  }
  .person__role {
    font-size: 13px;
    letter-spacing: 0.5px;
    margin-top: 4px;
  }
  .contact {
    position: absolute;
    right: 40px;
    top: 52px;
    list-style: none;
    color: var(--ink-light);
    font-size: 14px;
    letter-spacing: 0.4px;
  }
  .contact__item {
    display: flex;
    align-items: center;
    gap: 8px;
    margin-bottom: 6px;
  }
  .contact__icon {
    width: 14px;
    height: 14px;
    flex: none;
  }
</style>
</head>
<body>
<main class="canvas">

  <section class="card card--front" aria-label="Card front">
    <svg class="card__waves" viewBox="0 0 620 354" preserveAspectRatio="none" aria-hidden="true">
      <path d="M0 190 C150 196 230 262 360 262 C470 262 560 205 620 150 L620 354 L0 354 Z" fill="var(--violet-front)"/>
      <path d="M0 190 C150 196 230 262 360 262 C470 262 560 205 620 150" fill="none" stroke="var(--teal)" stroke-width="5"/>
    </svg>
    <div class="brand"><span class="brand__dot"></span>Veyla Health</div>
  </section>

  <section class="card card--back" aria-label="Card back">
    <svg class="card__waves" viewBox="0 0 620 354" preserveAspectRatio="none" aria-hidden="true">
      <path d="M0 320 C90 235 190 180 320 182 C450 184 560 230 620 262 L620 354 L0 354 Z" fill="var(--card-white)"/>
      <path d="M0 320 C90 235 190 180 320 182 C450 184 560 230 620 262" fill="none" stroke="var(--teal)" stroke-width="5"/>
    </svg>

    <ul class="contact">
      <li class="contact__item">
        <svg class="contact__icon" viewBox="0 0 14 14" aria-hidden="true">
          <circle cx="7" cy="7" r="7" fill="var(--teal)"/>
          <path d="M4.6 3.8 L5.8 3.6 L6.4 5.2 L5.6 5.8 C6 6.8 6.8 7.6 7.8 8 L8.4 7.2 L10 7.8 L9.8 9 C7 9.2 4.4 6.6 4.6 3.8 Z" fill="var(--violet-back)"/>
        </svg>
        0000000000
      </li>
      <li class="contact__item">
        <svg class="contact__icon" viewBox="0 0 14 14" aria-hidden="true">
          <circle cx="7" cy="7" r="7" fill="var(--teal)"/>
          <rect x="3.6" y="4.6" width="6.8" height="4.8" fill="none" stroke="var(--violet-back)" stroke-width="1"/>
          <path d="M3.6 4.6 L7 7.4 L10.4 4.6" fill="none" stroke="var(--violet-back)" stroke-width="1"/>
        </svg>
        sample@samplemail.com
      </li>
    </ul>

    <div class="person">
      <p class="person__name">Name Title</p>
      <p class="person__role">Designation</p>
    </div>

    <div class="brand"><span class="brand__dot"></span>Veyla Health</div>
  </section>

</main>
</body>
</html>
```